Plumbing Company After Business Card

Business card for a plumbing business that offers a variety of plumbing services including maintenance, domestic and commercial plumbing. My main focus is to offer high quality professional service. A logo on the card would be ideal. Any other questions feel free to email. Cheers

Looking for something modern and upmarket with preferably a matte black background

Business name is Crestline Plumbing and Gas

Industry/Entity Type

Plumbing

Contact Information for Business Card

Crestline Plumbing and Gas
Marcus Thorvale
0472519306
14 Karrabee Drive, Ascot 3550
crestlineplumbing@mailbay.com.au
ABN 64 915 207 338

Font styles to use
Sans Serif

Colors
1b1b1b
ffffff
3377b5

Requirements
Must have
• Domestic
• Commercial
• Maintenance

```html
<!DOCTYPE html>
<html lang="en">
<head>
<meta charset="utf-8">
<title>Crestline Plumbing and Gas – Business Card</title>
<link href="https://fonts.googleapis.com/css2?family=Lato:wght@400;700;900&display=swap" rel="stylesheet">
<style>
  :root {
    --page: #d9d9d9;
    --card: #1b1b1b;
    --card-deep: #0f0f0f;
    --photo-light: #5a5a5a;
    --photo-dark: #1e1e1e;
    --white: #ffffff;
    --soft: #bdbdbd;
    --blue: #3377b5;
    --icon-bg: #3a3a3a;
  }
  * { box-sizing: border-box; margin: 0; padding: 0; }
  ul { list-style: none; }
  html, body { width: 1200px; height: 913px; overflow: hidden; }
  body {
    background: var(--page);
    font-family: "Lato", sans-serif;
    display: flex;
    align-items: center;
    justify-content: center;
    gap: 50px;
  }
  .card {
    position: relative;
    width: 540px;
    height: 330px;
    background: linear-gradient(160deg, var(--card) 0%, var(--card-deep) 100%);
    border-radius: 6px;
    overflow: hidden;
    box-shadow: 0 14px 30px rgba(0,0,0,.35);
    color: var(--white);
  }
  .card__photo {
    position: absolute;
    inset: 0 0 0 35%;
    background: radial-gradient(ellipse at 55% 30%, var(--photo-light) 0%, var(--photo-dark) 60%, transparent 85%);
    opacity: .75;
  }
  .brand {
    position: absolute;
    display: flex;
    align-items: center;
    gap: 12px;
  }
  .brand__mark {
    width: 46px; height: 46px;
    border-radius: 50%;
    background: var(--blue);
    flex: none;
  }
  .brand__name {
    font-weight: 900;
    text-transform: uppercase;
    letter-spacing: 1px;
    line-height: 1.15;
    color: var(--white);
    white-space: nowrap;
  }
  .brand__line { display: block; }

  /* front */
  .card--front .brand { left: 50%; top: 96px; transform: translateX(-50%); }
  .card--front .brand__name { font-size: 24px; }
  .services {
    position: absolute;
    left: 0; right: 0; bottom: 58px;
    display: flex;
    justify-content: center;
    align-items: center;
    gap: 26px;
    font-size: 15px;
    line-height: 1;
    letter-spacing: 1.5px;
  }
  .services__item { display: block; }
  .services__dot {
    display: block;
    width: 6px; height: 6px;
    border-radius: 50%;
    background: var(--blue);
  }

  /* back */
  .card--back .brand { right: 30px; top: 44px; }
  .card--back .brand__name { font-size: 20px; }
  .person {
    position: absolute;
    left: 36px; top: 140px;
    padding-left: 14px;
    border-left: 4px solid var(--blue);
  }
  .person__name { font-size: 22px; letter-spacing: 1px; text-transform: uppercase; font-weight: 400; }
  .person__name strong { font-weight: 900; }
  .person__role { font-size: 11px; letter-spacing: 1.5px; color: var(--soft); }
  .contact {
    position: absolute;
    left: 54px; top: 210px;
    font-size: 13.5px;
    letter-spacing: .3px;
  }
  .contact__item { display: flex; align-items: center; gap: 12px; height: 24px; }
  .contact__icon {
    width: 20px; height: 20px; border-radius: 50%;
    background: var(--icon-bg);
    display: flex; align-items: center; justify-content: center;
    flex: none;
  }
  .contact__icon svg { width: 11px; height: 11px; fill: var(--white); }
</style>
</head>
<body>

<section class="card card--front">
  <div class="card__photo" role="img" aria-label="Dark monochrome photo of plumbing pipes and fittings with water droplets"></div>
  <div class="brand">
    <span class="brand__mark"></span>
    <span class="brand__name"><span class="brand__line">Crestline</span><span class="brand__line">Plumbing and Gas</span></span>
  </div>
  <div class="services">
    <span class="services__item">DOMESTIC</span>
    <span class="services__dot"></span>
    <span class="services__item">COMMERCIAL</span>
    <span class="services__dot"></span>
    <span class="services__item">MAINTENANCE</span>
  </div>
</section>

<section class="card card--back">
  <div class="card__photo" role="img" aria-label="Dark monochrome photo of plumbing pipes and fittings with water droplets"></div>
  <div class="brand">
    <span class="brand__mark"></span>
    <span class="brand__name"><span class="brand__line">Crestline</span><span class="brand__line">Plumbing and Gas</span></span>
  </div>
  <div class="person">
    <h1 class="person__name"><strong>Marcus</strong> Thorvale</h1>
    <p class="person__role">OWNER</p>
  </div>
  <ul class="contact">
    <li class="contact__item">
      <span class="contact__icon"><svg viewBox="0 0 12 12"><path d="M2.5 1l2 2-1 1.3a7 7 0 0 0 4.2 4.2L9 7.5l2 2-1.3 1.5C5.5 11 1 6.5 1 2.3z"/></svg></span>
      0472519306
    </li>
    <li class="contact__item">
      <span class="contact__icon"><svg viewBox="0 0 12 12"><rect x="3" y="1" width="6" height="3"/><rect x="1" y="4.5" width="10" height="4.5" rx="1"/><rect x="3" y="8" width="6" height="3"/></svg></span>
      ABN 64 915 207 338
    </li>
    <li class="contact__item">
      <span class="contact__icon"><svg viewBox="0 0 12 12"><path d="M1 3h10v6H1z M1 3l5 3.5L11 3" fill="none" stroke="#fff" stroke-width="1.2"/></svg></span>
      crestlineplumbing@mailbay.com.au
    </li>
    <li class="contact__item">
      <span class="contact__icon"><svg viewBox="0 0 12 12"><g fill="none" stroke="#fff" stroke-width="1"><circle cx="6" cy="6" r="4.8"/><ellipse cx="6" cy="6" rx="2" ry="4.8"/><path d="M1.2 6h9.6"/></g></svg></span>
      14 Karrabee Drive, Ascot 3550
    </li>
  </ul>
</section>

</body>
</html>
```